Redesign - Trifold Brochure - Adding new and fresh look.

I have attached what we currently have as a brochure but we need it to be redesigned. The information content is accurate but looking for fresh new design/layout. Please see the images attached. In tif and pdf format. If you need a different format to work please specify and will do my best to upload it.

Target Market(s)

Retail giveaways to educate customers.

Requirements
Must have
• New fresh look

```html
<!DOCTYPE html>
<html lang="en">
<head>
<meta charset="utf-8">
<title>Heartland Botanicals – CBD Trifold Brochure</title>
<link href="https://fonts.googleapis.com/css2?family=Lobster&family=Montserrat:wght@400;600;700&family=Open+Sans:wght@400;600;700&display=swap" rel="stylesheet">
<style>
:root{
  --backdrop:#93a74b;
  --paper:#ffffff;
  --green:#7ab532;
  --green-light:#a6cc3e;
  --green-dark:#5e9622;
  --orange:#f29322;
  --orange-deep:#e8731a;
  --brown:#4b2a14;
  --ink:#3a3a3a;
  --night:#0d2a3a;
}
*{box-sizing:border-box;margin:0;padding:0}
html,body{width:898px;height:1200px;overflow:hidden}
body{background:var(--backdrop);font-family:"Open Sans",Arial,sans-serif;color:var(--ink);position:relative}
.spread{position:absolute;left:59px;width:780px;height:560px;background:var(--paper);overflow:hidden;box-shadow:0 6px 18px rgba(0,0,0,.25)}
.spread--inside{top:27px}
.spread--outside{top:613px}
.panel{position:absolute;top:0;height:560px;width:260px}
.panel + .panel{border-left:1px solid rgba(0,0,0,.06)}
.abs{position:absolute}
.kicker{font-family:"Montserrat",sans-serif;color:var(--green);font-size:15px;font-weight:400;line-height:1}
.script{font-family:"Lobster",cursive;color:var(--brown);font-weight:400;line-height:1.05}
.body-copy{font-size:7.6px;line-height:1.4}
.accent{color:var(--green);font-family:"Montserrat",sans-serif;font-weight:600}
.accent-orange{color:var(--orange);font-family:"Montserrat",sans-serif;font-weight:700}
.photo{position:absolute;border-radius:50%;overflow:hidden}
.dot{position:absolute;border-radius:50%}

/* inside: what is cbd */
.relief-list{list-style:none;display:grid;grid-template-columns:1fr 1.3fr;gap:4px 10px}
.relief-list li{font-family:"Lobster",cursive;font-size:9.5px;color:var(--brown);position:relative;padding-left:13px}
.relief-list li::before{content:"";position:absolute;left:0;top:3px;border-left:7px solid var(--green);border-top:3.5px solid transparent;border-bottom:3.5px solid transparent}

/* inside: body infographic */
.callout{position:absolute;background:rgba(20,20,20,.82);color:#f1e5c8;font-size:6.2px;line-height:1.3;padding:5px 6px;text-align:center;border:1px solid rgba(255,255,255,.15)}
.nutrient-title{font-family:"Montserrat",sans-serif;font-weight:700;font-size:13px;color:var(--brown)}
.nutrient-list{list-style:none;margin-top:5px}
.nutrient-list li{font-family:"Montserrat",sans-serif;font-weight:600;font-size:8.5px;color:var(--brown);padding-left:14px;position:relative;margin-bottom:4px}
.nutrient-list li::before{content:"";position:absolute;left:0;top:2px;width:7px;height:7px;border-radius:50%;background:linear-gradient(135deg,var(--green) 50%,var(--orange) 50%)}
.strip{position:absolute;left:0;right:0;bottom:0;height:10px;background:var(--green)}

/* outside: faq */
.faq-q{font-family:"Montserrat",sans-serif;font-weight:700;font-size:9.5px;color:var(--orange);margin-top:9px}
.faq-a{font-size:7.6px;line-height:1.4}

/* outside: contact */
.panel--contact{background:linear-gradient(160deg,var(--green-light),var(--green) 55%,var(--green-dark))}
.contact-line{display:flex;gap:6px;align-items:flex-start;font-size:7.6px;color:#fff;font-weight:600;line-height:1.35}
.contact-line svg{flex:none;margin-top:1px}
.brand-name{font-family:"Montserrat",sans-serif;font-weight:600;color:var(--brown)}

/* outside: cover */
.cover-band{position:absolute;left:0;right:0;height:34px;background:var(--green);display:flex;align-items:center;justify-content:center}
</style>
</head>
<body>

<!-- ================= INSIDE SPREAD ================= -->
<section class="spread spread--inside">

  <!-- panel 1: What is CBD -->
  <div class="panel" style="left:0">
    <div class="abs" style="left:22px;top:26px;width:220px">
      <p class="kicker">What is</p>
      <h2 class="script" style="font-size:26px">CBD?</h2>
      <p class="body-copy" style="margin-top:8px">CBD stands for Canna-bi-dy-all. CBD is one of many compounds called phytocannabinoids that is found in various plant species. The industrial hemp plant is a plentiful source of CBD. When derived from industrial hemp, CBD with less than 0.03% THC by weight has no psychoactive properties but retains all of its positive bio benefits.</p>
      <p class="accent" style="font-size:10px;margin-top:12px">CBD is commonly used as relief from:</p>
      <ul class="relief-list" style="margin-top:9px">
        <li>Pain</li><li>Sleep Disorders</li>
        <li>Inflammation</li><li>Neurological Disorders</li>
        <li>Anxiety</li><li>Opiate Dependence</li>
      </ul>
    </div>
    <div class="dot" style="left:160px;top:300px;width:32px;height:32px;background:var(--orange)"></div>
    <div class="dot" style="left:100px;top:330px;width:42px;height:42px;background:var(--green-light)"></div>
    <div class="dot" style="left:150px;top:330px;width:190px;height:190px;background:var(--green)"></div>
    <div class="dot" style="left:205px;top:470px;width:80px;height:80px;background:var(--orange-deep)"></div>
    <div class="photo" role="img" aria-label="Photo of golden CBD oil dripping from a dropper onto a glass dish on a wooden table" style="left:-40px;top:360px;width:270px;height:270px;background:radial-gradient(circle at 55% 40%,#f5c34a,#b8701c 45%,#5a3312 85%)"></div>
  </div>

  <!-- panels 2–3: How does CBD work -->
  <div class="panel" style="left:260px;width:520px">
    <svg class="abs" style="left:0;top:0" width="520" height="300" viewBox="0 0 520 300" aria-hidden="true">
      <path d="M0 0H520V235C430 200 300 250 190 280C110 300 40 290 0 260Z" fill="var(--orange)"/>
    </svg>
    <svg class="abs" style="left:0;top:0" width="520" height="300" viewBox="0 0 520 300" role="img" aria-label="Illustration of a glowing translucent human body and a red brain showing where cannabinoid receptors are found">
      <defs>
        <linearGradient id="bodyGlow" x1="0" y1="0" x2="1" y2="0">
          <stop offset="0" stop-color="#0f3e4f"/>
          <stop offset=".45" stop-color="var(--night)"/>
          <stop offset=".75" stop-color="#7a1d12"/>
          <stop offset="1" stop-color="#e7641a"/>
        </linearGradient>
      </defs>
      <path d="M0 0H520V229C430 194 300 244 190 274C110 294 40 284 0 254Z" fill="url(#bodyGlow)"/>
    </svg>
    <div class="callout" style="left:185px;top:46px;width:70px">CB2 receptors are predominantly found in the immune system.</div>
    <div class="callout" style="left:200px;top:112px;width:80px">CB1 and CB2 receptors are found on the surface of your body that affect your endocannabinoid system.</div>
    <div class="callout" style="left:230px;top:190px;width:80px">CB2 receptors are responsible for the regulation of inflammation which in turn reduces pain.</div>
    <div class="callout" style="left:405px;top:140px;width:92px">CB1 receptors are found primarily in the brain controlling memory processing, motor regulation, appetite, pain sensation, mood, and sleep.</div>
    <div class="dot" style="left:470px;top:225px;width:34px;height:34px;background:var(--orange)"></div>
    <div class="dot" style="left:455px;top:258px;width:22px;height:22px;background:var(--green)"></div>

    <div class="abs" style="left:30px;top:298px;width:470px">
      <p class="kicker" style="font-size:13px">How Does <span style="color:var(--orange);font-weight:700;font-size:18px">CBD</span></p>
      <h2 class="script" style="font-size:21px">Work In Your Body?</h2>
      <p class="body-copy" style="margin-top:6px">Your body produces certain natural compounds called cannabinoids that are used to regulate functions for your entire body. Inside your body there is a processing network for cannabinoids called your Endocannabinoid System. CBD mimics the natural cannabinoids produced by your body and stimulates central receptors found on the surface of cells in your body that effect your ECS. These cells are mainly located in the central nervous system and the immune system. This reaction caused by the introduction of CBD helps balance and maintain and restore your body's natural function.</p>
      <p class="accent" style="font-size:10px;margin-top:10px">There are many other benefits from using CBD and hemp products. Hemp products are:</p>
      <div style="display:flex;gap:90px;margin-top:10px">
        <div>
          <p class="nutrient-title">HIGH IN</p>
          <ul class="nutrient-list">
            <li>Omega 3 and 6 Fatty Acids</li>
            <li>Vitamins A &amp; E</li>
            <li>Calcium, Iron &amp; Antioxidants</li>
          </ul>
        </div>
        <div>
          <p class="nutrient-title">LOW IN</p>
          <ul class="nutrient-list">
            <li>Saturated Fats</li>
            <li>Cholesterol</li>
            <li>Carbohydrates</li>
          </ul>
        </div>
      </div>
    </div>
    <div class="strip"></div>
  </div>
</section>

<!-- ================= OUTSIDE SPREAD ================= -->
<section class="spread spread--outside">

  <!-- panel 1: FAQ -->
  <div class="panel" style="left:0">
    <div class="dot" style="left:-10px;top:10px;width:70px;height:70px;background:var(--green)"></div>
    <div class="dot" style="left:-20px;top:95px;width:110px;height:110px;background:var(--orange)"></div>
    <div class="dot" style="left:190px;top:150px;width:20px;height:20px;background:var(--green-light)"></div>
    <div class="photo" role="img" aria-label="Photo of a glass jar of hemp oil beside a burlap sack of hemp seeds and a spoon of hemp powder" style="left:45px;top:-10px;width:170px;height:170px;background:radial-gradient(circle at 60% 35%,#e7c94a,#a78a4c 45%,#5b5140 85%);border:3px solid #fff"></div>
    <div class="abs" style="left:20px;top:178px;width:225px">
      <p style="font-family:'Montserrat',sans-serif;font-weight:700;font-size:8px;color:var(--brown);line-height:1.35">Hemp derived products are widely thought to be the most nutritionally complete supplement source in the world.</p>
      <p class="kicker" style="font-size:11px;color:var(--orange);margin-top:10px">The Most Common Questions</p>
      <h2 class="script" style="font-size:17px">Associated with CBD Use:</h2>
      <p class="faq-q">Will I get "high" or feel "loaded"?</p>
      <p class="faq-a">The answer is, "No." Industrial hemp derived CBD will not make you feel euphoric. If you feel this way from a CBD product, it does not solely contain CBD and may contain synthetics or other compounds not listed on the label and should not be used.</p>
      <p class="faq-q">Is it legal?</p>
      <p class="faq-a">Yes. Industrial hemp derived CBD contains very low to no THC levels which is the compound that makes Marijuana illegal. Industrial hemp products containing levels of THC ranging from 0% to 0.03% can be purchased from regular retailers and are legal in all 50 states.</p>
      <p class="faq-q">How can I take CBD?</p>
      <p class="faq-a">CBD comes in many forms: Tinctures,</p>
      <p class="faq-q">How much CBD should I take?</p>
      <p class="faq-a">Edibles, vaporizable liquids, capsules, powders, as well as topical creams and salves.</p>
    </div>
  </div>

  <!-- panel 2: contact -->
  <div class="panel panel--contact" style="left:260px">
    <div class="abs" role="img" aria-label="Product photo of two supplement jars and two dropper bottles of CBD tincture" style="left:30px;top:50px;width:200px;height:120px;border-radius:14px;background:linear-gradient(180deg,rgba(255,255,255,.9),#f3e3c3 60%,#e8a54a)"></div>
    <div class="abs" style="left:0;right:0;top:205px;height:26px;background:#fff"></div>
    <div class="dot" style="left:85px;top:178px;width:90px;height:90px;background:#fff;box-shadow:0 2px 6px rgba(0,0,0,.2);display:flex;align-items:center;justify-content:center;text-align:center">
      <span class="brand-name" style="font-size:9px;line-height:1.2">Heartland<br>Botanicals</span>
    </div>
    <div class="abs" style="left:22px;top:290px;width:220px">
      <h2 class="script" style="font-size:22px;text-align:center">Get in touch</h2>
      <p style="font-size:7.6px;color:#fff;margin-top:10px;line-height:1.35">If you would like to receive more information or purchase Heartland Botanicals products, please contact:</p>
      <div class="contact-line" style="margin-top:6px">
        <svg width="9" height="7" viewBox="0 0 9 7"><rect width="9" height="7" rx="1" fill="var(--brown)"/><path d="M0 0L4.5 4L9 0" stroke="#fff" stroke-width=".8" fill="none"/></svg>
        <span>customerservice@heartlandbotanicals.com</span>
      </div>
      <p style="font-size:7.6px;color:#fff;margin-top:10px;line-height:1.35">If you would like to become a wholesale partner of Heartland Botanicals, please send all wholesale inquiries to:</p>
      <div class="contact-line" style="margin-top:6px">
        <svg width="9" height="7" viewBox="0 0 9 7"><rect width="9" height="7" rx="1" fill="var(--brown)"/><path d="M0 0L4.5 4L9 0" stroke="#fff" stroke-width=".8" fill="none"/></svg>
        <span>wholesale@heartlandbotanicals.com</span>
      </div>
      <div class="contact-line" style="margin-top:6px">
        <svg width="9" height="11" viewBox="0 0 9 11"><path d="M4.5 0C2 0 0 2 0 4.5C0 7.5 4.5 11 4.5 11S9 7.5 9 4.5C9 2 7 0 4.5 0Z" fill="var(--brown)"/><circle cx="4.5" cy="4.5" r="1.6" fill="#fff"/></svg>
        <span>418 W. Maple Ridge Avenue, Suite 3<br>Fairview, OK 73737</span>
      </div>
      <div class="contact-line" style="margin-top:6px">
        <svg width="9" height="9" viewBox="0 0 9 9"><path d="M1.5 0L3.3 2.3L2.4 3.5C3 4.8 4.2 6 5.5 6.6L6.7 5.7L9 7.5L7.6 9C3.5 8.6 .4 5.5 0 1.4Z" fill="var(--brown)"/></svg>
        <span>(844) 555-0142</span>
      </div>
    </div>
  </div>

  <!-- panel 3: cover -->
  <div class="panel" style="left:520px">
    <div class="abs" style="left:0;width:260px;top:28px;text-align:center">
      <p style="display:flex;align-items:center;justify-content:center;gap:6px">
        <span class="dot" style="position:static;display:inline-block;width:14px;height:14px;background:var(--orange)"></span>
        <span class="brand-name" style="font-size:12px">Heartland Botanicals</span>
      </p>
      <p class="script" style="font-size:10px;color:var(--orange);margin-top:8px">Healthier Living Through Quality Products</p>
    </div>
    <div class="dot" style="left:150px;top:120px;width:110px;height:110px;background:var(--green-light)"></div>
    <div class="dot" style="left:180px;top:205px;width:90px;height:90px;background:var(--orange)"></div>
    <div class="photo" role="img" aria-label="Photo of a dense field of tall green hemp plants" style="left:30px;top:85px;width:190px;height:190px;background:radial-gradient(circle at 45% 40%,#6fae3e,#2f6a24 55%,#1c3f17);border:3px solid #fff"></div>
    <div class="abs" style="left:26px;top:305px;width:220px">
      <p class="kicker" style="color:var(--orange);font-size:16px">Can CBD</p>
      <h1 class="script" style="font-size:23px">Products Help Me?</h1>
      <p style="font-family:'Montserrat',sans-serif;color:var(--orange);font-size:11px;margin-top:4px;line-height:1.25">Understanding Your<br>Endocannabinoid System</p>
    </div>
    <div class="cover-band" style="top:430px">
      <span class="script" style="font-size:15px">Putting the Pieces Together</span>
    </div>
  </div>
</section>

</body>
</html>
```